Automotive eCommerce Business looking for a business card design

Looking for a clean and simple business card design. Our company name is "Harbor Crest Auto" and we are a company specializing in the ecommerce sales of automotive parts, specifically for pick up trucks and large SUVs. Our company colours are red, black, and white.

Feel free to use the logo provided or create a new logo that you seem fit. Looking forward to your creative ideas!

Industry/Entity Type

Automotive

Contact Information for Business Card

We were thinking of a possibly two-sided design featuring just the logo and company name on one side, and personal information on the other side. Single sided designs will be considered as well.

Font styles to use
Serif
Sans Serif
Decorative

Colors
ec1f27
ffffff
000000

Requirements
Must have
• Space for employee's name, title, phone number and email address, along with the company address and website somewhere.

```html
<!DOCTYPE html>
<html lang="en">
<head>
<meta charset="utf-8">
<title>Harbor Crest Auto – Business Card</title>
<link href="https://fonts.googleapis.com/css2?family=Work+Sans:wght@400;500;600&display=swap" rel="stylesheet">
<style>
  :root {
    --red: #ec1f27;
    --black: #000000;
    --white: #ffffff;
    --backdrop: #3a3a3a;
    --muted: #d9d9d9;
  }
  * { box-sizing: border-box; margin: 0; padding: 0; }
  html, body {
    width: 1200px; height: 900px; overflow: hidden;
    background: var(--backdrop);
    font-family: "Work Sans", Arial, sans-serif;
  }
  .canvas {
    width: 1200px; height: 900px;
    display: flex; flex-direction: column; align-items: center; justify-content: center;
    gap: 36px;
  }
  .card {
    position: relative;
    width: 700px; height: 400px;
    background: var(--black);
    overflow: hidden;
    box-shadow: 0 10px 28px rgba(0,0,0,.45);
  }
  /* front side */
  .card--front { display: flex; align-items: center; justify-content: center; }
  .brand { display: flex; align-items: center; gap: 14px; }
  .brand__mark { width: 22px; height: 22px; background: var(--red); }
  .brand__name {
    color: var(--white); font-weight: 600; text-transform: uppercase;
    letter-spacing: .08em; line-height: 1.1;
  }
  .card--front .brand__name { font-size: 40px; }
  .card--front .brand__mark { width: 30px; height: 30px; }

  /* back side */
  .card--back .brand { position: absolute; left: 40px; top: 48px; }
  .card--back .brand__name { font-size: 27px; }

  .rule {
    position: absolute; left: 30px; top: 196px;
    width: 560px; height: 2px; background: var(--red);
  }
  .person { position: absolute; right: 44px; top: 166px; text-align: right; }
  .person__name {
    color: var(--red); font-size: 26px; font-weight: 500;
    text-transform: uppercase; letter-spacing: .02em; line-height: 1;
  }
  .person__title {
    color: var(--muted); font-size: 17px; margin-top: 10px; letter-spacing: .04em;
  }
  .contacts {
    position: absolute; left: 34px; top: 214px;
    list-style: none; color: var(--white); font-size: 16px; line-height: 22px;
  }
  .contacts li { display: flex; align-items: center; gap: 10px; }
  .contacts svg { width: 11px; height: 11px; flex: none; }
  .contacts .accent { color: var(--red); }
  .swoosh { position: absolute; left: 0; bottom: 0; width: 700px; height: 110px; }
</style>
</head>
<body>
<main class="canvas">
  <section class="card card--front" aria-label="Card front">
    <div class="brand">
      <span class="brand__mark"></span>
      <span class="brand__name">Harbor Crest Auto Ltd</span>
    </div>
  </section>

  <section class="card card--back" aria-label="Card back">
    <div class="brand">
      <span class="brand__mark"></span>
      <span class="brand__name">Harbor Crest Auto Ltd</span>
    </div>

    <div class="rule"></div>

    <div class="person">
      <p class="person__name">Daniel Ashford</p>
      <p class="person__title">Director</p>
    </div>

    <ul class="contacts">
      <li>
        <svg viewBox="0 0 12 12" aria-hidden="true"><path d="M2 1h3l1 3-1.5 1a6 6 0 0 0 2.5 2.5L8 6l3 1v3a1 1 0 0 1-1 1A9 9 0 0 1 1 2a1 1 0 0 1 1-1z" fill="var(--red)"/></svg>
        555.014.2325
      </li>
      <li>
        <svg viewBox="0 0 12 12" aria-hidden="true"><rect x="3" y="0.5" width="6" height="11" rx="1" fill="none" stroke="var(--red)" stroke-width="1.3"/></svg>
        555.019.5887
      </li>
      <li>
        <svg viewBox="0 0 12 12" aria-hidden="true"><rect x="0.7" y="2" width="10.6" height="8" fill="none" stroke="var(--red)" stroke-width="1.3"/><path d="M1 2.5l5 4 5-4" fill="none" stroke="var(--red)" stroke-width="1.3"/></svg>
        info@harborcrestauto.com
      </li>
      <li>
        <svg viewBox="0 0 12 12" aria-hidden="true"><circle cx="6" cy="6" r="5" fill="none" stroke="var(--red)" stroke-width="1.3"/><path d="M1 6h10M6 1c-2.5 3-2.5 7 0 10M6 1c2.5 3 2.5 7 0 10" fill="none" stroke="var(--red)" stroke-width="1"/></svg>
        <span>www.<span class="accent">harborcrestauto</span>.com</span>
      </li>
    </ul>

    <svg class="swoosh" viewBox="0 0 700 110" aria-hidden="true">
      <path d="M0 66 L300 79 L0 76 Z" fill="var(--white)"/>
      <path d="M0 84 L300 90 C335 91 345 70 385 66 L700 60 L700 110 L0 110 Z" fill="var(--red)"/>
    </svg>
  </section>
</main>
</body>
</html>
```